Icon Redesign

We need a new and consistent icon design for our new e-learning platform, velunor.com.
Just few hints:
- no 3D effects
- no shadows
- no gradients/no glossy effects
- outlines/frames very reduced - best no outlines/frames
- more plain, simple forms
- redesign of the icons: you can forget our symbols if you don't like them other symbolis for the mentioned reasons are highly welcome.
What is velunor? Velunor is an online school for financial trading. It provides users with strategies for successful online trading and works by giving access to educational content. It is aimed at beginners to online trading. We are currently in the beta phase and we will soon launch this page in three languages (EN, DE, RU) but in future we want launch further 15 languages.
We  expect the design to have a consistent look&feel and fit into our lean and plain interface. In the brief  we explain the icon types and the function of each icon. Please redesign the eleven icons and unify their styling.  Be aware that we will have users from 18 countries. The icons need to be universal and work for all the different cultural backgrounds.
You can find more details in our brief.

Updates
Hi alltogether,
just another hint as it come out from discussions that we had today.
What we also mean with redesign of the icons: you can forget our symbols if you don't like them other symbols for the described usage (see the table in our briefing) are highly welcome.
KR,

Industry/Entity Type
Financial
Requirements
Must have
- We want to use these icons also for many other e-learning platforms like for a poker school or health and fitness, etc. They must fit to several styles and topics.
Nice to have
- You can base your redesign on the style of our illustrations, but that’s not a must. You can use the colors of our design manual (attached)
Should not have
- - no 3D effects
- no shadows

```html
<!DOCTYPE html>
<html lang="en">
<head>
<meta charset="utf-8">
<title>Velunor – Icon and message styles</title>
<link rel="stylesheet" href="https://fonts.googleapis.com/css2?family=Noto+Sans:wght@400;700&family=Tinos&display=swap">
<style>
:root{
  --ink:#1e1e1e; --muted:#555; --panel:#f4f4f4; --line:#9a9a9a;
  --err-bg:#f9dcdc; --err-line:#e04848; --err-ink:#c81414;
  --ok-bg:#def5c9; --ok-line:#8fd24f; --ok-ink:#4b8a12;
  --warn-bg:#fde9c6; --warn-line:#f0b030; --warn-ink:#d88700;
  --info-bg:#e8e8e8; --info-line:#9c9c9c;
  --blue:#6cb2ef; --blue-line:#3d8fd6; --link:#2a78c2; --btn-grey:#cfd3d6;
  --def-bg:#fdf9d9; --def-bar:#f5d000; --tip-bg:#dff0d0; --green:#4fa832;
  --icon-dark:#1e2328; --gear:#3a86c6; --palette:#e9e9e9;
}
*{box-sizing:border-box;margin:0;padding:0}
html,body{width:1200px;height:824px;overflow:hidden;background:#fff}
body{font-family:"Noto Sans",Verdana,sans-serif;color:var(--ink)}
.sheet{position:absolute;left:0;top:0;width:1160px;height:797px;transform:scale(1.0345,1.0339);transform-origin:0 0;border:1px solid #555;background:#fff}
.sheet>*{position:absolute}
.ico{display:inline-block;vertical-align:middle}
.msg{left:19px;width:556px;height:26px;border:1px solid;font-size:11.5px;display:flex;align-items:center;padding-left:8px;gap:10px}
.msg.error{top:10px;background:var(--err-bg);border-color:var(--err-line);color:var(--err-ink)}
.msg.ok{top:258px;background:var(--ok-bg);border-color:var(--ok-line);color:var(--ok-ink)}
.msg.warn{top:334px;background:var(--warn-bg);border-color:var(--warn-line);color:var(--warn-ink)}
.msg.info{top:411px;background:var(--info-bg);border-color:var(--info-line);color:#3a3a3a;padding-left:8px}
.form-panel{left:19px;top:36px;width:556px;height:211px;background:var(--panel)}
.field-row{position:absolute;left:4px;width:548px;height:24px;font-size:12.5px;display:flex;align-items:center;padding-left:5px}
.field-row.bad{background:var(--err-bg);color:var(--err-ink)}
.input{position:absolute;left:168px;width:377px;height:23px;background:#fff;border:1px solid #9a9a9a;font-size:13px;letter-spacing:1px;padding-left:3px;display:flex;align-items:center}
.bad .input{border-color:var(--err-line);color:#333}
.hint{position:absolute;left:168px;font-size:11px;color:var(--err-ink)}
.check{position:absolute;left:168px;display:flex;align-items:center;gap:6px;font-size:12px}
.box{width:12px;height:12px;border:1px solid #555;background:#fff;display:flex;align-items:center;justify-content:center}
.btn{position:absolute;height:22px;border:1px solid;font-size:12.5px;display:flex;align-items:center;justify-content:center}
.btn.grey{background:var(--btn-grey);border-color:#8a8e92;color:#222}
.btn.blue{background:var(--blue);border-color:var(--blue-line);color:#123}
.pw-panel{left:19px;width:556px;height:40px;background:var(--panel);font-size:12.5px}
.pw-panel span{position:absolute;top:12px}
.pw-panel .ico{position:absolute;right:16px;top:12px}
.caption{font-size:12px;color:#222}
h2.block-title{font-size:14px;font-weight:700}
.def-box{left:742px;top:28px;width:415px;height:65px;background:var(--def-bg);border-left:4px solid var(--def-bar);margin-left:12px;width:403px;padding:3px 6px;font-size:10.5px;line-height:16px}
.body-note{font-size:10.5px;line-height:16px}
.tip-band{left:742px;top:180px;width:415px;height:14px;background:var(--tip-bg);font-size:10.5px;display:flex;align-items:center;gap:6px}
.tabs{left:739px;top:337px;height:24px;display:flex;font-size:10px;font-weight:700;background:#ddd;width:140px;overflow:hidden;border-top:1px solid #ccc}
.tabs div{height:23px;display:flex;align-items:center;padding:0 6px;border-right:1px solid #bbb;white-space:nowrap}
.tabs .home{background:#fff;padding:0 8px}
.edit-strip{left:0;top:511px;width:566px;height:82px;background:#c7c7c7}
.edit-row{position:absolute;left:5px;width:555px;height:30px;background:var(--panel);font-size:12.5px}
.edit-row .lbl{position:absolute;left:8px;top:6px}
.edit-row .input{left:163px;top:4px;width:285px;height:22px;letter-spacing:0;font-size:12.5px}
.edit-row .btn{top:5px;width:39px;height:20px}
.note{font-family:"Tinos","Times New Roman",serif;font-size:10.5px;color:#111}
.forum-title{left:14px;top:600px;font-size:15px;font-weight:700}
.section{font-size:9px;font-weight:700;color:#777}
.rule{height:1px;background:#888}
.topic{font-size:10px;font-weight:700;color:var(--link)}
.art{border-radius:4px}
.count{font-size:9px;color:#666;display:flex;align-items:center;gap:2px}
.side{font-size:8.5px;color:#333}
.palette{left:1028px;top:664px;width:112px;height:92px;background:var(--palette);border:1px solid #d4d4d4;border-radius:4px}
.palette svg{position:absolute}
</style>
</head>
<body>
<svg width="0" height="0" style="position:absolute">
  <defs>
    <symbol id="i-star" viewBox="0 0 12 12"><path d="M6 .5l1.7 3.6 3.8.4-2.9 2.6.9 3.9L6 9 2.5 11l.9-3.9L.5 4.5l3.8-.4z" fill="#f5c400"/></symbol>
    <symbol id="i-home" viewBox="0 0 12 12"><path d="M6 1L.5 6H2v5h3V8h2v3h3V6h1.5z" fill="var(--icon-dark)"/></symbol>
    <symbol id="i-go" viewBox="0 0 12 12"><rect x="1" y="1" width="10" height="10" rx="1" fill="var(--icon-dark)"/><path d="M3 5.2h3.3V3.4L9 6 6.3 8.6V6.8H3z" fill="#fff"/></symbol>
    <symbol id="i-warn" viewBox="0 0 12 12"><circle cx="6" cy="6" r="5" fill="none" stroke="#f0a000" stroke-width="1.4"/><rect x="5.3" y="2.8" width="1.4" height="4" fill="#f0a000"/><rect x="5.3" y="7.8" width="1.4" height="1.4" fill="#f0a000"/></symbol>
    <symbol id="i-tip" viewBox="0 0 12 12"><rect x="1.5" y=".5" width="9" height="11" fill="var(--green)"/><rect x="5.3" y="2.3" width="1.4" height="1.4" fill="#fff"/><rect x="5.3" y="4.5" width="1.4" height="5" fill="#fff"/></symbol>
    <symbol id="i-save" viewBox="0 0 12 12"><rect x="1" y="1" width="10" height="10" rx="1" fill="var(--icon-dark)"/><rect x="3.5" y="7" width="5" height="4" fill="#fff"/></symbol>
    <symbol id="i-error" viewBox="0 0 12 12"><path d="M6 1l5.2 9.5H.8z" fill="none" stroke="#d92020" stroke-width="1.4" stroke-linejoin="round"/><rect x="5.3" y="4.2" width="1.4" height="3.2" fill="#d92020"/><rect x="5.3" y="8.1" width="1.4" height="1.3" fill="#d92020"/></symbol>
    <symbol id="i-gear" viewBox="0 0 12 12"><path d="M5 .5h2l.3 1.6 1.2.5 1.4-.9 1.4 1.4-.9 1.4.5 1.2 1.6.3v2l-1.6.3-.5 1.2.9 1.4-1.4 1.4-1.4-.9-1.2.5L7 11.5H5l-.3-1.6-1.2-.5-1.4.9L.7 8.9l.9-1.4-.5-1.2L-.5 6V5l1.6-.3.5-1.2-.9-1.4L2.1.7l1.4.9L4.7 1.1z" fill="currentColor"/><circle cx="6" cy="6" r="1.8" fill="#fff"/></symbol>
    <symbol id="i-ok" viewBox="0 0 12 12"><circle cx="6" cy="6" r="5" fill="none" stroke="#3fa032" stroke-width="1.4"/><path d="M3.5 6.2l1.8 1.8 3.3-3.5" fill="none" stroke="#3fa032" stroke-width="1.4"/></symbol>
    <symbol id="i-comment" viewBox="0 0 12 12"><path d="M1 1.5h10v7H5l-2.5 2.3V8.5H1z" fill="#5f6a73"/><rect x="3" y="4.5" width="1.2" height="1.2" fill="#fff"/><rect x="5.4" y="4.5" width="1.2" height="1.2" fill="#fff"/><rect x="7.8" y="4.5" width="1.2" height="1.2" fill="#fff"/></symbol>
    <symbol id="i-search" viewBox="0 0 12 12"><circle cx="5" cy="5" r="3.2" fill="none" stroke="#5f6a73" stroke-width="1.6"/><path d="M7.3 7.3l3.5 3.5" stroke="#5f6a73" stroke-width="2"/></symbol>
    <symbol id="i-pencil" viewBox="0 0 12 12"><path d="M9 1.2l1.8 1.8-6.9 6.9-2.4.6.6-2.4z" fill="none" stroke="#666" stroke-width="1"/><path d="M7.6 2.6l1.8 1.8" stroke="#666"/></symbol>
    <symbol id="i-eye" viewBox="0 0 12 12"><path d="M.5 6C2 3.5 4 2.5 6 2.5S10 3.5 11.5 6C10 8.5 8 9.5 6 9.5S2 8.5.5 6z" fill="#6a747c"/><circle cx="6" cy="6" r="1.7" fill="#fff"/></symbol>
    <symbol id="i-x" viewBox="0 0 12 12"><path d="M2 2l8 8M10 2l-8 8" stroke="#1e2328" stroke-width="1.8"/></symbol>
  </defs>
</svg>

<main class="sheet">
  <div class="msg error"><svg class="ico" width="13" height="13"><use href="#i-error"/></svg>Error in line three, error in line 5.</div>
  <section class="form-panel">
    <div class="field-row" style="top:8px">Current password<div class="input">++++++++</div></div>
    <div class="field-row" style="top:40px">New password<div class="input">++++++++</div></div>
    <div class="field-row bad" style="top:67px">Reply new password<div class="input" style="top:1px">++++++++</div></div>
    <div class="hint" style="top:93px">The passwords do not match</div>
    <div class="field-row bad" style="top:123px;height:27px">Fallback
      <div class="check"><span class="box"><svg width="10" height="10" viewBox="0 0 10 10"><path d="M1.5 5l2.3 2.4L8.5 2" fill="none" stroke="#111" stroke-width="1.6"/></svg></span>Use English as fallback for all languages</div>
    </div>
    <div class="hint" style="top:150px">Combination not possible</div>
    <div class="btn grey" style="left:329px;top:180px;width:89px">Cancel</div>
    <div class="btn blue" style="left:429px;top:180px;width:116px">Change Password</div>
  </section>

  <div class="msg ok"><svg class="ico" width="13" height="13"><use href="#i-ok"/></svg>Your password has been succesfully updated</div>
  <div class="pw-panel" style="top:284px"><span style="left:9px">Password</span><span style="left:168px;letter-spacing:1px">+++++++++</span><svg class="ico" width="14" height="14"><use href="#i-pencil"/></svg></div>
  <div class="msg warn"><svg class="ico" width="13" height="13"><use href="#i-warn"/></svg>Your password is not safe!</div>
  <div class="pw-panel" style="top:360px"><span style="left:9px">Password</span><span style="left:168px;letter-spacing:1px">+++++++++</span><svg class="ico" width="14" height="14"><use href="#i-pencil"/></svg></div>
  <div class="msg info">Please validate your e-mail</div>
  <div class="pw-panel" style="top:437px"><span style="left:9px">Password</span><span style="left:168px;letter-spacing:1px">+++++++++</span><svg class="ico" width="14" height="14"><use href="#i-pencil"/></svg></div>

  <p class="caption" style="left:603px;top:17px">Error Red</p>
  <p class="caption" style="left:603px;top:264px">Confirmation Green</p>
  <p class="caption" style="left:603px;top:339px">Warning Yellow</p>
  <p class="caption" style="left:603px;top:416px">Info Grey</p>

  <h2 class="block-title" style="left:742px;top:6px">Definition wrapper</h2>
  <svg style="left:741px;top:30px" width="12" height="12"><use href="#i-star"/></svg>
  <div class="def-box"><b>OHLC</b><br>The <b>o</b>pening price, highest price, lowest price and closing price of a given period is often referred to as the <b>OHLC</b>. Charts that display this information are often called <b style="color:var(--err-ink)">OHLC charts</b>.</div>
  <p class="body-note" style="left:742px;top:101px;width:415px">The definition wrapper for short definition of concepts which are used to explain another concept.</p>
  <h2 class="block-title" style="left:742px;top:155px">Tip wrapper</h2>
  <div class="tip-band"><svg class="ico" width="13" height="13" style="margin-left:-1px"><use href="#i-tip"/></svg>Entering an additional tip here.</div>
  <p class="body-note" style="left:742px;top:200px">Still undefined.</p>

  <nav class="tabs"><div class="home"><svg width="12" height="12"><use href="#i-home"/></svg></div><div>Learn to trade</div><div>Brokers</div></nav>

  <section class="edit-strip">
    <div class="edit-row" style="top:6px"><span class="lbl">Edit view 7</span><div class="input">Text setting</div>
      <div class="btn grey" style="left:457px"><svg width="12" height="12"><use href="#i-x"/></svg></div>
      <div class="btn blue" style="left:506px"><svg width="12" height="12"><use href="#i-go"/></svg></div></div>
    <div class="edit-row" style="top:48px"><span class="lbl">Edit view 7</span><div class="input">Text setting</div>
      <div class="btn grey" style="left:457px"><svg width="12" height="12"><use href="#i-x"/></svg></div>
      <div class="btn blue" style="left:506px"><svg width="12" height="12"><use href="#i-save"/></svg></div></div>
  </section>
  <svg style="left:560px;top:520px" width="170" height="70"><path d="M8 10h37l25 25M8 58h37l25-25h90" fill="none" stroke="#111"/></svg>
  <span class="note" style="left:644px;top:544px;text-decoration:underline">Submit/Save</span>

  <h2 class="forum-title">Forum</h2>
  <span class="section" style="left:13px;top:632px">Beta launch</span>
  <div class="rule" style="left:13px;top:643px;width:417px"></div>
  <div class="art" role="img" aria-label="Feedback illustration: speech bubbles with minus and plus" style="left:14px;top:648px;width:44px;height:46px;background:linear-gradient(135deg,#6fb3e6,#1f5f92)"></div>
  <svg style="left:55px;top:648px" width="7" height="7"><path d="M0 0h7v7z" fill="#999"/></svg>
  <span class="topic" style="left:68px;top:650px">Feedback</span>
  <span class="count" style="left:364px;top:687px">284<svg width="11" height="11"><use href="#i-eye"/></svg></span>
  <span class="count" style="left:410px;top:687px">14<svg width="12" height="12"><use href="#i-comment"/></svg></span>

  <span class="section" style="left:13px;top:713px">Community</span>
  <div class="rule" style="left:13px;top:723px;width:417px"></div>
  <div class="art" role="img" aria-label="Community illustration: two hands shaking" style="left:13px;top:735px;width:50px;height:34px;background:linear-gradient(135deg,#8fc6ec,#2c6ea6)"></div>
  <svg style="left:55px;top:729px" width="7" height="7"><path d="M0 0h7v7z" fill="#999"/></svg>
  <span class="topic" style="left:68px;top:730px">Introduce yourself</span>
  <span class="count" style="left:367px;top:768px">76<svg width="11" height="11"><use href="#i-eye"/></svg></span>
  <span class="count" style="left:414px;top:768px">3<svg width="12" height="12"><use href="#i-comment"/></svg></span>

  <svg style="left:260px;top:630px;color:var(--gear)" width="220" height="150">
    <path d="M83 13h80M83 13v24M83 25h80M83 37h80M8 25h75M14 83h95l10-9M10 115h135l20 23" fill="none" stroke="#111" stroke-width=".8"/>
    <svg x="160" y="9" width="10" height="10" style="color:#1e2328"><use href="#i-gear"/></svg>
    <svg x="160" y="21" width="10" height="10"><use href="#i-gear"/></svg>
    <svg x="160" y="33" width="10" height="10"><use href="#i-gear"/></svg>
  </svg>
  <span class="note" style="left:345px;top:631px">Normal State</span>
  <span class="note" style="left:345px;top:643px">Mouse Over</span>
  <span class="note" style="left:345px;top:655px">Pressed State</span>
  <span class="note" style="left:267px;top:643px">Gear Icon</span>
  <span class="note" style="left:275px;top:698px">Viewed Icon</span>
  <span class="note" style="left:270px;top:729px">Comments Icon</span>
  <div style="left:432px;top:652px;width:36px;height:13px;border:1px solid #3d8fd6;background:#fff;font-size:8px;display:flex;align-items:center;gap:2px;padding-left:2px"><svg width="8" height="8"><use href="#i-pencil"/></svg>Edit</div>

  <span class="side" style="left:444px;top:600px;font-weight:700;text-decoration:underline;color:#555">HOT TOP</span>
  <span class="side" style="left:444px;top:617px">There is n</span>
  <span class="side" style="left:444px;top:633px;color:var(--link)">Show more</span>
  <div style="left:444px;top:676px;width:36px;height:120px;border-left:1px solid #ccc;border-top:1px solid #ccc;overflow:hidden">
    <div style="font-size:9px;font-weight:700;padding:6px 7px">Find u</div>
    <div style="position:absolute;left:18px;top:34px;width:6px;height:6px;background:var(--link)"></div>
    <div class="side" style="position:absolute;left:9px;top:44px;font-size:6px">velunor</div>
    <div class="side" style="position:absolute;left:9px;top:75px;font-size:7px">895 peo</div>
    <div role="img" aria-label="Member profile photo" style="position:absolute;left:9px;top:92px;width:26px;height:28px;background:#8d8a86"></div>
  </div>

  <section class="palette" aria-label="Icon set">
    <svg style="left:7px;top:7px" width="13" height="13"><use href="#i-star"/></svg>
    <svg style="left:27px;top:7px" width="13" height="13"><use href="#i-home"/></svg>
    <svg style="left:47px;top:7px" width="13" height="13"><use href="#i-go"/></svg>
    <svg style="left:7px;top:27px" width="13" height="13"><use href="#i-warn"/></svg>
    <svg style="left:27px;top:27px" width="13" height="13"><use href="#i-tip"/></svg>
    <svg style="left:47px;top:27px" width="13" height="13"><use href="#i-save"/></svg>
    <svg style="left:7px;top:47px" width="13" height="13"><use href="#i-error"/></svg>
    <svg style="left:27px;top:47px;color:var(--gear)" width="13" height="13"><use href="#i-gear"/></svg>
    <svg style="left:47px;top:47px;color:var(--icon-dark)" width="13" height="13"><use href="#i-gear"/></svg>
    <svg style="left:67px;top:47px;color:var(--gear)" width="13" height="13"><use href="#i-gear"/></svg>
    <svg style="left:7px;top:67px" width="13" height="13"><use href="#i-ok"/></svg>
    <svg style="left:27px;top:67px" width="13" height="13"><use href="#i-comment"/></svg>
    <svg style="left:47px;top:67px" width="13" height="13"><use href="#i-search"/></svg>
    <svg style="left:67px;top:67px" width="13" height="13"><use href="#i-pencil"/></svg>
    <svg style="left:87px;top:67px" width="13" height="13"><use href="#i-eye"/></svg>
  </section>
</main>
</body>
</html>
```